Poster design for a company operating care homes in the UK showcasing our core values

We need a poster to display in our care homes showcasing our new core values:

Purpose
We are driven by a clear understanding of why we do what we do: to enrich lives, honour legacies and make a meaningful difference every day, for our residents, their families, our colleagues and our community.

Excellence
We hold ourselves to the highest standards, delivering exceptional care and creating an environment where both residents and staff can thrive.

Openness
We build trust through honest, respectful communication, welcoming feedback, sharing ideas, and embracing change as a path to continuous growth.

Passion
We are passionate about delivering exceptional care. We take pride in what we do and in making a real difference in people’s lives.

Learning
We are committed to personal and professional growth; empowering each other through ongoing development, reflection, and shared knowledge.

Empathy
We actively listen and seek to understand before being understood, recognising the unique stories, feelings, and needs of others.

I have attached a small graphic that we would like you try to incorporate, in addition to our company logo. Please theme the rest of the poster around our company colours.

```html
<!DOCTYPE html>
<html lang="en">
<head>
<meta charset="utf-8">
<title>Our Core Values – Poster Variants</title>
<link href="https://fonts.googleapis.com/css2?family=Montserrat:wght@600;700;800&family=Poppins:wght@400;500&display=swap" rel="stylesheet">
<style>
  :root{
    --navy:#3a5471;
    --peach:#eca785;
    --board:#c9cacc;
    --panel-light:#f2f2f2;
    --white:#ffffff;
    --card-end:#f3f3f3;
    --body-text:#4b4f55;
  }
  *{box-sizing:border-box;margin:0;padding:0}
  html,body{width:1163px;height:1200px;overflow:hidden;background:var(--board)}
  .board{position:relative;width:1163px;height:1200px}
  .poster{position:absolute;left:95px;width:973px;height:463px;background:var(--white);
    box-shadow:6px 8px 10px rgba(0,0,0,.28)}
  .poster--light{top:99px}
  .poster--dark{top:638px}
  .poster__field{position:absolute;left:0;top:0;width:100%;height:373px}
  .poster--light .poster__field{background:var(--panel-light)}
  .poster--dark .poster__field{background:var(--navy)}
  .poster__title{position:absolute;top:27px;left:0;width:100%;text-align:center;
    font-family:'Montserrat',sans-serif;font-weight:800;font-size:31px;letter-spacing:.3px;color:var(--navy)}
  .poster--dark .poster__title{color:var(--white)}
  .value{position:absolute;width:254px;height:81px}
  .value__backing{position:absolute;left:-9px;top:-9px;width:98px;height:99px;border-radius:13px}
  .backing--navy{background:var(--navy)}
  .backing--peach{background:var(--peach)}
  .value__card{position:absolute;inset:0;border-radius:10px;
    background:linear-gradient(90deg,var(--white) 0%,var(--card-end) 100%);
    box-shadow:0 2px 4px rgba(0,0,0,.22)}
  .value__icon{position:absolute;left:11px;top:20px;width:42px;height:42px}
  .value__rule{position:absolute;left:64px;top:12px;width:1px;height:57px}
  .rule--navy{background:var(--navy)}
  .rule--peach{background:var(--peach)}
  .value__text{position:absolute;left:72px;top:14px;right:10px}
  .value__name{font-family:'Montserrat',sans-serif;font-weight:700;font-size:11px;
    text-transform:uppercase;letter-spacing:.2px;line-height:14px;margin-bottom:1px}
  .value__name .initial{font-size:15px}
  .name--navy{color:var(--navy)}
  .name--peach{color:var(--peach)}
  .value__desc{font-family:'Poppins',sans-serif;font-weight:400;font-size:6.1px;line-height:7.3px;color:var(--body-text)}
  .col-1{left:59px}.col-2{left:354px}.col-3{left:668px}
  .row-1{top:105px}.row-2{top:243px}
  .brand{position:absolute;left:0;right:0;top:395px;display:flex;justify-content:center;align-items:center;gap:9px}
  .brand__mark{width:16px;height:16px;background:var(--peach)}
  .brand__name{font-family:'Montserrat',sans-serif;font-weight:600;font-size:27px;letter-spacing:.5px;color:var(--navy)}
</style>
</head>
<body>
<svg width="0" height="0" style="position:absolute" aria-hidden="true">
  <defs>
    <symbol id="icon-target" viewBox="0 0 40 40">
      <g fill="none" stroke="#3a5471" stroke-width="3"><circle cx="17" cy="23" r="13"/><circle cx="17" cy="23" r="7.5"/></g>
      <circle cx="17" cy="23" r="2.5" fill="#3a5471"/>
      <path d="M17 23 L33 7" stroke="#eca785" stroke-width="3.5" stroke-linecap="round"/>
      <path d="M30 3 L31 9 L37 10 L33 14 L27 12 Z" fill="#eca785"/>
    </symbol>
    <symbol id="icon-award" viewBox="0 0 40 40">
      <path d="M13 24 L8 36 L13 34 L16 38 L19 28 Z M27 24 L32 36 L27 34 L24 38 L21 28 Z" fill="#eca785"/>
      <circle cx="20" cy="15" r="12" fill="#fff" stroke="#3a5471" stroke-width="2.2"/>
      <circle cx="20" cy="15" r="7.5" fill="none" stroke="#eca785" stroke-width="2"/>
      <path d="M20 10.5 l1.4 3 3.2.3-2.4 2.1.7 3.2-2.9-1.7-2.9 1.7.7-3.2-2.4-2.1 3.2-.3z" fill="#3a5471"/>
    </symbol>
    <symbol id="icon-bulb" viewBox="0 0 40 40">
      <g stroke="#3a5471" stroke-width="2.2" stroke-linecap="round" fill="none">
        <path d="M14 27 C9 23 9 13 20 11 C31 13 31 23 26 27 L26 30 L14 30 Z"/>
        <path d="M15 33 H25 M16.5 36 H23.5"/>
        <path d="M20 3 V6 M8 8 L10 10 M32 8 L30 10 M3 20 H6 M34 20 H37"/>
      </g>
      <circle cx="20" cy="20" r="5" fill="none" stroke="#eca785" stroke-width="3" stroke-dasharray="2.5 1.4"/>
      <circle cx="20" cy="20" r="2" fill="#eca785"/>
    </symbol>
    <symbol id="icon-passion" viewBox="0 0 40 40">
      <path d="M20 6 C26 11 30 15 28 22 C26 27 14 27 12 22 C10 17 14 14 16 10 C17 13 18 14 20 13 C21 11 20 8 20 6 Z" fill="none" stroke="#eca785" stroke-width="2"/>
      <path d="M20 25 C14 20 15 15 18 16 C19 16.5 20 18 20 18 C20 18 21 16.5 22 16 C25 15 26 20 20 25 Z" fill="#eca785"/>
      <path d="M5 32 C9 29 13 29 17 31 L24 31 C26 31 26 34 24 34 L17 34 M24 33 L32 28 C34 27 36 29 34 31 L26 37 H12 L7 36" fill="none" stroke="#3a5471" stroke-width="2" stroke-linejoin="round" stroke-linecap="round"/>
      <path d="M7 6 l1 2 2 1-2 1-1 2-1-2-2-1 2-1z M34 16 l1 2 2 1-2 1-1 2-1-2-2-1 2-1z" fill="#3a5471"/>
    </symbol>
    <symbol id="icon-learning" viewBox="0 0 40 40">
      <rect x="3" y="13" width="26" height="18" rx="1.5" fill="none" stroke="#3a5471" stroke-width="2.4"/>
      <path d="M13 31 V35 M19 31 V35 M10 36 H22" stroke="#3a5471" stroke-width="2.4" stroke-linecap="round"/>
      <path d="M20 7 L33 3 L38 10 L25 14 Z" fill="#eca785"/>
      <path d="M24 13 V19 C28 20 32 19 34 16 V10" fill="none" stroke="#eca785" stroke-width="2"/>
      <path d="M37 10 V20" stroke="#eca785" stroke-width="1.6"/>
    </symbol>
    <symbol id="icon-empathy" viewBox="0 0 40 40">
      <circle cx="20" cy="20" r="16" fill="none" stroke="#3a5471" stroke-width="2.2"/>
      <path d="M20 30 C9 22 11 12 16 12 C18 12 20 15 20 15 C20 15 22 12 24 12 C29 12 31 22 20 30 Z" fill="#eca785"/>
      <path d="M15 22 L19 19 L23 22" fill="none" stroke="#fff" stroke-width="1.6" stroke-linecap="round"/>
    </symbol>
  </defs>
</svg>

<main class="board">

  <!-- Light variant -->
  <section class="poster poster--light">
    <div class="poster__field">
      <h1 class="poster__title">OUR CORE VALUES</h1>

      <article class="value col-1 row-1">
        <div class="value__backing backing--navy"></div>
        <div class="value__card">
          <svg class="value__icon"><use href="#icon-target"/></svg>
          <span class="value__rule rule--peach"></span>
          <div class="value__text">
            <h2 class="value__name name--navy"><span class="initial">P</span>urpose</h2>
            <p class="value__desc">We are driven by a clear understanding of why we do what we do: to enrich lives, honour legacies and make a meaningful difference every day, for our residents, their families, our colleagues and our community.</p>
          </div>
        </div>
      </article>

      <article class="value col-2 row-1">
        <div class="value__backing backing--peach"></div>
        <div class="value__card">
          <svg class="value__icon"><use href="#icon-award"/></svg>
          <span class="value__rule rule--navy"></span>
          <div class="value__text" style="top:19px">
            <h2 class="value__name name--peach"><span class="initial">E</span>xcellence</h2>
            <p class="value__desc">We hold ourselves to the highest standards, delivering exceptional care and creating an environment where both residents and staff can thrive.</p>
          </div>
        </div>
      </article>

      <article class="value col-3 row-1">
        <div class="value__backing backing--navy"></div>
        <div class="value__card">
          <svg class="value__icon"><use href="#icon-bulb"/></svg>
          <span class="value__rule rule--peach"></span>
          <div class="value__text">
            <h2 class="value__name name--navy"><span class="initial">O</span>penness</h2>
            <p class="value__desc">We build trust through honest, respectful communication, welcoming feedback, sharing ideas, and embracing change as a path to continuous growth.</p>
          </div>
        </div>
      </article>

      <article class="value col-1 row-2">
        <div class="value__backing backing--peach"></div>
        <div class="value__card">
          <svg class="value__icon"><use href="#icon-passion"/></svg>
          <span class="value__rule rule--navy"></span>
          <div class="value__text" style="top:18px">
            <h2 class="value__name name--peach"><span class="initial">P</span>assion</h2>
            <p class="value__desc">We are passionate about delivering exceptional care. We take pride in what we do and in making a real difference in people’s lives.</p>
          </div>
        </div>
      </article>

      <article class="value col-2 row-2">
        <div class="value__backing backing--navy"></div>
        <div class="value__card">
          <svg class="value__icon"><use href="#icon-learning"/></svg>
          <span class="value__rule rule--peach"></span>
          <div class="value__text" style="top:18px">
            <h2 class="value__name name--navy"><span class="initial">L</span>earning</h2>
            <p class="value__desc">We are committed to personal and professional growth; empowering each other through ongoing development, reflection, and shared knowledge.</p>
          </div>
        </div>
      </article>

      <article class="value col-3 row-2">
        <div class="value__backing backing--peach"></div>
        <div class="value__card">
          <svg class="value__icon"><use href="#icon-empathy"/></svg>
          <span class="value__rule rule--navy"></span>
          <div class="value__text" style="top:18px">
            <h2 class="value__name name--peach"><span class="initial">E</span>mpathy</h2>
            <p class="value__desc">We actively listen and seek to understand before being understood, recognising the unique stories, feelings, and needs of others.</p>
          </div>
        </div>
      </article>
    </div>
    <div class="brand"><span class="brand__mark"></span><span class="brand__name">HALDEN</span></div>
  </section>

  <!-- Dark variant -->
  <section class="poster poster--dark">
    <div class="poster__field">
      <h1 class="poster__title">OUR CORE VALUES</h1>

      <article class="value col-1 row-1">
        <div class="value__backing backing--peach"></div>
        <div class="value__card">
          <svg class="value__icon"><use href="#icon-target"/></svg>
          <span class="value__rule rule--peach"></span>
          <div class="value__text">
            <h2 class="value__name name--navy"><span class="initial">P</span>urpose</h2>
            <p class="value__desc">We are driven by a clear understanding of why we do what we do: to enrich lives, honour legacies and make a meaningful difference every day, for our residents, their families, our colleagues and our community.</p>
          </div>
        </div>
      </article>

      <article class="value col-2 row-1">
        <div class="value__backing backing--peach"></div>
        <div class="value__card">
          <svg class="value__icon"><use href="#icon-award"/></svg>
          <span class="value__rule rule--navy"></span>
          <div class="value__text" style="top:19px">
            <h2 class="value__name name--peach"><span class="initial">E</span>xcellence</h2>
            <p class="value__desc">We hold ourselves to the highest standards, delivering exceptional care and creating an environment where both residents and staff can thrive.</p>
          </div>
        </div>
      </article>

      <article class="value col-3 row-1">
        <div class="value__backing backing--peach"></div>
        <div class="value__card">
          <svg class="value__icon"><use href="#icon-bulb"/></svg>
          <span class="value__rule rule--peach"></span>
          <div class="value__text">
            <h2 class="value__name name--navy"><span class="initial">O</span>penness</h2>
            <p class="value__desc">We build trust through honest, respectful communication, welcoming feedback, sharing ideas, and embracing change as a path to continuous growth.</p>
          </div>
        </div>
      </article>

      <article class="value col-1 row-2">
        <div class="value__backing backing--peach"></div>
        <div class="value__card">
          <svg class="value__icon"><use href="#icon-passion"/></svg>
          <span class="value__rule rule--navy"></span>
          <div class="value__text" style="top:18px">
            <h2 class="value__name name--peach"><span class="initial">P</span>assion</h2>
            <p class="value__desc">We are passionate about delivering exceptional care. We take pride in what we do and in making a real difference in people’s lives.</p>
          </div>
        </div>
      </article>

      <article class="value col-2 row-2">
        <div class="value__backing backing--peach"></div>
        <div class="value__card">
          <svg class="value__icon"><use href="#icon-learning"/></svg>
          <span class="value__rule rule--peach"></span>
          <div class="value__text" style="top:18px">
            <h2 class="value__name name--navy"><span class="initial">L</span>earning</h2>
            <p class="value__desc">We are committed to personal and professional growth; empowering each other through ongoing development, reflection, and shared knowledge.</p>
          </div>
        </div>
      </article>

      <article class="value col-3 row-2">
        <div class="value__backing backing--peach"></div>
        <div class="value__card">
          <svg class="value__icon"><use href="#icon-empathy"/></svg>
          <span class="value__rule rule--navy"></span>
          <div class="value__text" style="top:18px">
            <h2 class="value__name name--peach"><span class="initial">E</span>mpathy</h2>
            <p class="value__desc">We actively listen and seek to understand before being understood, recognising the unique stories, feelings, and needs of others.</p>
          </div>
        </div>
      </article>
    </div>
    <div class="brand"><span class="brand__mark"></span><span class="brand__name">HALDEN</span></div>
  </section>

</main>
</body>
</html>
```